Business Card

I need a business card that really pops for a potential customer or person who refers a personal injury lead. I want to highlight our office locations, but only address that needs to be on the card is my office's main address. I want a sleek, modern and minimalist design.

```html
<!DOCTYPE html>
<html lang="en">
<head>
<meta charset="utf-8">
<title>Northfield Injury Lawyers – Business Card</title>
<link href="https://fonts.googleapis.com/css2?family=Jost:wght@400&display=swap" rel="stylesheet">
<style>
  :root {
    --stage: #8e8e8e;
    --card-front: #ffffff;
    --card-back: #3a3a3a;
    --ink: #2f2f2f;
    --ink-soft: #5c5c5c;
    --rule: #8a8a8a;
    --back-ink: #b9b9b9;
  }
  * { margin: 0; padding: 0; box-sizing: border-box; }
  html, body { width: 1200px; height: 1200px; overflow: hidden; }
  body {
    background: var(--stage);
    font-family: "Jost", "Futura", sans-serif;
    font-weight: 400;
    position: relative;
  }
  .card {
    position: absolute;
    left: 281px;
    width: 642px;
    height: 353px;
    border-radius: 19px;
  }
  .card--front { top: 195px; background: var(--card-front); color: var(--ink); }
  .card--back { top: 639px; background: var(--card-back); }

  .brand {
    position: absolute;
    text-align: center;
    white-space: nowrap;
    font-weight: 400;
    line-height: 1;
  }
  .card--front .brand { left: 30px; width: 280px; top: 168px; font-size: 20px; color: var(--ink); }
  .card--back .brand { left: 0; width: 642px; top: 158px; font-size: 38px; color: var(--back-ink); }

  .divider {
    position: absolute;
    left: 320px; top: 83px;
    width: 1px; height: 200px;
    background: var(--rule);
  }

  .contact { position: absolute; left: 349px; top: 80px; }
  .contact__name { font-size: 24px; font-weight: 400; line-height: 1; letter-spacing: 0.01em; color: var(--ink); }
  .contact__role { font-size: 16px; line-height: 1; color: var(--ink-soft); margin-top: 6px; }
  .contact__address { font-size: 14.5px; line-height: 20.5px; color: var(--ink-soft); margin-top: 13px; letter-spacing: 0.02em; }
  .contact__list { list-style: none; margin-top: 9px; }
  .contact__list li {
    display: flex; align-items: center;
    font-size: 14.5px; line-height: 20.5px; color: var(--ink-soft); letter-spacing: 0.02em;
  }
  .contact__list svg { width: 11px; height: 11px; margin-right: 11px; fill: var(--ink); flex: none; }
</style>
</head>
<body>

<section class="card card--front" aria-label="Card front">
  <p class="brand">Northfield Injury Lawyers</p>
  <div class="divider"></div>
  <div class="contact">
    <h1 class="contact__name">DANIEL HARPER</h1>
    <p class="contact__role">Injury Lawyer</p>
    <p class="contact__address">4820 Alder Lane<br>Brookfield, CT 06804</p>
    <ul class="contact__list">
      <li><svg viewBox="0 0 12 12" aria-hidden="true"><path d="M2.5 0.8 4.4 2.9 3.5 4.3C4.2 5.8 5.9 7.6 7.6 8.4L9 7.5 11.2 9.5 10 11.2C5.5 11.2 0.8 6.5 0.8 2Z"/></svg>555.410.2287</li>
      <li><svg viewBox="0 0 12 12" aria-hidden="true"><path d="M3 0h6a1 1 0 0 1 1 1v10a1 1 0 0 1-1 1H3a1 1 0 0 1-1-1V1a1 1 0 0 1 1-1Zm0.4 1.6v7.8h5.2V1.6ZM6 10a0.6 0.6 0 1 0 0 1.2A0.6 0.6 0 0 0 6 10Z"/></svg>555.732.9164</li>
      <li><svg viewBox="0 0 12 12" aria-hidden="true"><path d="M3 0h6v3H3ZM1 3.8h10a1 1 0 0 1 1 1V9H9.5v3h-7V9H0V4.8a1 1 0 0 1 1-1Zm2.8 4.7v2.3h4.4V8.5Z"/></svg>555.268.4503</li>
      <li><svg viewBox="0 0 12 12" aria-hidden="true"><path d="M0.5 2h11v0.8L6 6.6 0.5 2.8ZM0.5 4.2 6 8l5.5-3.8V10h-11Z"/></svg>info@northfieldinjurylaw.com</li>
      <li><svg viewBox="0 0 12 12" aria-hidden="true"><path d="M6 0a6 6 0 1 0 0 12A6 6 0 0 0 6 0Zm0 1.2c.8 0 1.6 1.7 1.8 4.2H4.2C4.4 2.9 5.2 1.2 6 1.2ZM1.3 6.6h1.7c.1 1.5.4 2.8.9 3.6A4.8 4.8 0 0 1 1.3 6.6Zm0-1.2A4.8 4.8 0 0 1 3.9 1.8c-.5.8-.8 2.1-.9 3.6Zm4.7 5.4c-.8 0-1.6-1.7-1.8-4.2h3.6c-.2 2.5-1 4.2-1.8 4.2Zm2.1-.6c.5-.8.8-2.1.9-3.6h1.7a4.8 4.8 0 0 1-2.6 3.6ZM9 5.4c-.1-1.5-.4-2.8-.9-3.6a4.8 4.8 0 0 1 2.6 3.6Z"/></svg>northfieldinjurylaw.com</li>
    </ul>
  </div>
</section>

<section class="card card--back" aria-label="Card back">
  <p class="brand">Northfield Injury Lawyers</p>
</section>

</body>
</html>
```